Verpackungen für Display Schutzglas
Vielen Dank für die tolle Zusammenarbeit, vom Anfang bis zum Ende war es uns eine Freude die Verpackung bzw. das Design zusammen zu gestalten.
Zielgruppe
Wir verkaufen Smartphone und Tabletzubehör. Für unseren Shop (Ladengeschäft) brauchen wir eine Verpackung für unser Display Schutzglas.
Aufgabenstellung
Wir möchten eine Verpackung die auf der Vorderseite sehr einfach gestaltet ist. Hier bitte nur auf das wesentliche hinweisen. Auf der Rückseite alles weitere wie Installation und Inhalt. Wir möchte einen Ausschnitt auf der Vorderseite durch den man den Inhalt erkennen kann. Bei den Farben bitte an die des Logos halten. Grundfarbe der Verpackung kann frei gewählt werden. Beispiel der Verpackung siehe jpg. Maße (BXH) 9,5 cm x 18 cm

```html
<!DOCTYPE html>
<html lang="de">
<head>
<meta charset="utf-8">
<title>Kavelo Mobile – Verpackung Premium Glasschutz</title>
<link rel="stylesheet" href="https://fonts.googleapis.com/css2?family=Montserrat:wght@300;400;600;700&display=swap">
<style>
  :root {
    --lime: #9ec310;
    --lime-light: #b5d617;
    --white: #ffffff;
    --paper: #f4f4f3;
    --ink: #1d1d1d;
    --grey: #9a9a9a;
    --bg: #e4e4e2;
  }
  * { margin: 0; padding: 0; box-sizing: border-box; }
  html, body { width: 1200px; height: 960px; overflow: hidden; }
  body {
    background: var(--bg);
    font-family: "Montserrat", sans-serif;
    position: relative;
  }
  .panel {
    position: absolute;
    top: 80px;
    width: 420px;
    height: 800px;
    overflow: hidden;
  }
  .brand {
    display: flex;
    align-items: center;
    gap: 10px;
    font-weight: 700;
    font-size: 26px;
    letter-spacing: 1px;
    text-transform: uppercase;
  }
  .brand-mark {
    width: 26px; height: 26px;
    border: 3px solid currentColor;
    border-radius: 4px;
  }

  /* Front */
  .front { left: 60px; background: var(--white); }
  .front .brand { position: absolute; top: 44px; left: 36px; color: var(--ink); }
  .front .window {
    position: absolute;
    top: 130px; left: 36px;
    width: 348px; height: 460px;
    border-radius: 14px;
    background: linear-gradient(160deg, #efefee 0%, #e2e2e0 45%, #1e2a36 46%, #2d3f4f 100%);
  }
  .front .tagline {
    position: absolute;
    left: 36px; right: 36px; bottom: 110px;
    text-align: right;
  }
  .front .tagline-main { color: var(--lime); font-weight: 700; font-size: 30px; }
  .front .tagline-sub { color: var(--grey); font-weight: 300; font-size: 24px; margin-top: 4px; }
  .front .edge-band {
    position: absolute; left: 0; right: 0; bottom: 0; height: 60px;
    background: var(--lime);
  }

  /* Back */
  .back { left: 520px; background: var(--lime-light); color: var(--white); padding: 44px 36px; }
  .back .brand { color: var(--white); }
  .back .title { margin-top: 34px; font-weight: 700; font-size: 26px; }
  .back .subtitle { font-weight: 400; font-size: 21px; margin-top: 2px; }
  .back .intro { margin-top: 22px; font-size: 14px; line-height: 1.55; text-align: justify; }
  .back .steps-heading { margin-top: 26px; font-weight: 700; font-size: 15px; letter-spacing: 1px; }
  .back .steps { list-style: none; margin-top: 14px; }
  .back .step { display: flex; gap: 14px; font-size: 13px; line-height: 1.5; margin-bottom: 12px; }
  .back .step-num {
    flex: 0 0 26px; height: 26px;
    border: 2px solid var(--white);
    border-radius: 50%;
    display: flex; align-items: center; justify-content: center;
    font-weight: 600; font-size: 12px;
  }

  /* Side */
  .side { left: 980px; width: 160px; display: flex; }
  .side-band { height: 100%; }
  .side-band.green { width: 40px; background: var(--lime); }
  .side-band.white {
    width: 80px; background: var(--paper);
    display: flex; flex-direction: column; align-items: center; justify-content: space-between;
    padding: 26px 0;
  }
  .side .vertical {
    writing-mode: vertical-rl;
    white-space: nowrap;
  }
  .side .brand { font-size: 20px; color: var(--ink); }
  .side .brand-mark { width: 20px; height: 20px; border-width: 2px; }
  .side .claim { font-size: 15px; color: var(--grey); font-weight: 300; }
  .side .claim strong { color: var(--lime); font-weight: 700; }
  .side .address { font-size: 10px; color: #555; line-height: 1.5; }
  .side .address strong { color: var(--ink); font-weight: 700; }
</style>
</head>
<body>

<section class="panel front">
  <div class="brand"><span class="brand-mark"></span>Kavelo Mobile</div>
  <div class="window" role="img" aria-label="Sichtfenster mit Smartphone und aufgelegtem Schutzglas"></div>
  <div class="tagline">
    <div class="tagline-main">Premium Glasschutz</div>
    <div class="tagline-sub">Schütze dein Smartphone</div>
  </div>
  <div class="edge-band"></div>
</section>

<section class="panel back">
  <div class="brand"><span class="brand-mark"></span>Kavelo Mobile</div>
  <h1 class="title">Premium Glasschutz</h1>
  <p class="subtitle">Schütze dein Smartphone</p>
  <p class="intro">Premium Glasschutz für dein Smartphone Display. Schütze dein Smartphone vor ungewollten Kratzern und Beschädigungen mit Premium Glasschutz.</p>
  <h2 class="steps-heading">ANLEITUNG:</h2>
  <ol class="steps">
    <li class="step"><span class="step-num">1</span><span>Reinige dein Display gründlich. (Tücher befindend sich in der Packung)</span></li>
    <li class="step"><span class="step-num">2</span><span>Entferne Staub mit dem beigefügten Aufkleber.</span></li>
    <li class="step"><span class="step-num">3</span><span>Nun die Folie vom Displayschutz vorsichtig entfernen und dabei jeglichen Kontakt zur Unterseite vermeiden.</span></li>
    <li class="step"><span class="step-num">4</span><span>Richte den Displayschutz auf Deinem Smartphone aus.</span></li>
    <li class="step"><span class="step-num">5</span><span>Drücke den Displayschutz nun in der Mitte an dein Smartphone. Premium Displayschutz fixiert sich automatisch.</span></li>
    <li class="step"><span class="step-num">6</span><span>Entferne mit der beigefügten Rakel kleine Blasen.</span></li>
  </ol>
</section>

<section class="panel side">
  <div class="side-band green"></div>
  <div class="side-band white">
    <div class="brand vertical"><span class="brand-mark"></span>Kavelo Mobile</div>
    <div class="claim vertical"><strong>Premium Glasschutz</strong> - Schütze dein Smartphone</div>
    <div class="address vertical">Kavelo Mobile<br>Lindenweg 8<br>20095 Hamburg<br><strong>Hergestellt in Deutschland</strong></div>
  </div>
  <div class="side-band green"></div>
</section>

</body>
</html>
```